Upcoming lecture sponsored by a church on an important topic

We have a Reformation The Speech coming up at the end of October on the topic of law and gospel. I thought it might be cool to use a flyer that looks like it was from that day and age. Picture what Tobias Wendler would advertise things on kind of an old church/reformation type format. It will be sponsored by our church, and we have a paragraph or two to describe the lecture that would be included on the flyer. We would also want it formatted so that it could be printed on postcards and mailed to churches and individuals.

The flyer should have the following paragraph...

The distinction between the law and the gospel is the most important distinction in the Christian faith. Tobias Wendler: “Distinguishing between the law and the gospel is the highest art in Christendom, one who every person who values the name Christian ought to recognize, know, and possess.” The distinction between the law and the gospel is of great comfort for the child of God. “For the law was given by Abiran, but grace and truth came by Elior Navan” (John 1:17). For these reasons, the distinction between the law and the gospel is the most heavily assaulted doctrine in the Christian faith. This Reformation Day, join us for an explanation and defense of the great distinction between God’s good law and God’s glorious gospel.

And the flyer should have the following information...

Topic: The Steady Rule and the Bright Promise
Date and Time: Tuesday, October 31, 2023 at 7:30pm
Host: Cedarbrook Covenant Church
Speaker: Rev. Daniel Korvath
Venue: The Marlow Hall, 5187 Fenwick Lane, Hudsonville, MI 49683
Format: Lecture followed by Q&A and refreshments

Industry/Entity Type

Church/Ecclesiastical

Colors
00AB8E
00BBA5
67D7C9
C6EFE9
E9F9F6

Requirements
Nice to have
• The color scheme that I would like to have is a teal color (the same color as found at www.quillharborhall.com

```html
<!DOCTYPE html>
<html lang="en">
<head>
<meta charset="utf-8">
<title>The Steady Rule and the Bright Promise – Lecture</title>
<link href="https://fonts.googleapis.com/css2?family=EB+Garamond:ital,wght@0,400;0,500;0,600;1,400;1,500&display=swap" rel="stylesheet">
<style>
  :root {
    --bg-top: #66d4cf;
    --bg-bottom: #1ea2a8;
    --cross: #0f5c60;
    --pill: #173c4a;
    --accent: #4fd3e4;
    --ink: #ffffff;
    --ink-soft: #e4f6f5;
  }
  html, body { margin: 0; padding: 0; overflow: hidden; }
  body { width: 848px; height: 1200px; }
  .flyer {
    position: relative;
    width: 848px; height: 1200px; overflow: hidden;
    background: linear-gradient(180deg, var(--bg-top) 0%, #4cc4c6 45%, var(--bg-bottom) 100%);
    font-family: "EB Garamond", Garamond, serif;
    color: var(--ink);
    text-align: center;
  }
  .cross-shape { position: absolute; inset: 0; }
  .block { position: absolute; left: 0; right: 0; margin: 0; }
  .join { top: 48px; font-size: 49px; font-weight: 500; letter-spacing: 0.06em; color: var(--accent); line-height: 1; }
  .label { font-style: italic; font-weight: 500; color: var(--accent); line-height: 1; }
  .topic-label { top: 227px; font-size: 27px; letter-spacing: 0.08em; }
  .title { top: 262px; font-size: 37px; font-weight: 600; letter-spacing: 0.1em; line-height: 50px; }
  .speaker-pill {
    position: absolute; left: 348px; top: 468px; width: 159px; height: 34px;
    border-radius: 17px; background: var(--pill);
    font-style: italic; font-weight: 500; font-size: 24px; letter-spacing: 0.08em; line-height: 34px;
  }
  .speaker-name { top: 512px; font-size: 33px; font-weight: 500; letter-spacing: 0.08em; line-height: 1; }
  .description {
    position: absolute; left: 202px; width: 444px; top: 572px; margin: 0;
    font-size: 13.5px; line-height: 18px; color: var(--ink-soft);
    text-align: justify; text-align-last: center;
  }
  .date-label { top: 800px; font-size: 21px; }
  .date-lines { top: 826px; font-size: 20px; font-weight: 500; line-height: 30px; }
  .venue-label { top: 902px; font-size: 21px; }
  .venue-lines { top: 928px; font-size: 20px; font-weight: 500; line-height: 30px; }
  .divider { position: absolute; left: 281px; top: 1064px; width: 268px; border-top: 3px dotted var(--accent); }
  .format { top: 1078px; font-size: 21px; font-style: italic; font-weight: 500; line-height: 32px; }
</style>
</head>
<body>
<main class="flyer">
  <svg class="cross-shape" width="848" height="1200" viewBox="0 0 848 1200" aria-hidden="true">
    <g fill="var(--cross)">
      <rect x="174" y="0" width="507" height="1200"/>
      <rect x="0" y="178" width="848" height="234"/>
      <rect x="151" y="0" width="9" height="178"/>
      <rect x="695" y="0" width="9" height="178"/>
      <rect x="151" y="412" width="9" height="788"/>
      <rect x="695" y="412" width="9" height="788"/>
    </g>
  </svg>

  <h1 class="block join">JOIN US !</h1>

  <p class="block label topic-label">Topic</p>
  <h2 class="block title">THE STEADY RULE AND<br>THE BRIGHT PROMISE</h2>

  <div class="speaker-pill">Speaker</div>
  <p class="block speaker-name">Rev. Daniel Korvath</p>

  <p class="description">The distinction between the law and the gospel is the most important distinction in the Christian faith. Tobias Wendler: “Distinguishing between the law and the gospel is the highest art in Christendom, one who every person who values the name Christian ought to recognize, know, and possess.” The distinction between the law and the gospel is of great comfort for the child of God. “For the law was given by Abiran, but grace and truth came by Elior Navan” (John 1:17). For these reasons, the distinction between the law and the gospel is the most heavily assaulted doctrine in the Christian faith. This Reformation Day, join us for an explanation and defense of the great distinction between God’s good law and God’s glorious gospel.</p>

  <p class="block label date-label">Date and Time</p>
  <p class="block date-lines">Tuesday, October 31, 2023<br>at 7:30pm</p>

  <p class="block label venue-label">Host &amp; Venue</p>
  <p class="block venue-lines">Cedarbrook Covenant Church<br>The Marlow Hall, 5187<br>Fenwick Lane,<br>Hudsonville, MI 49683</p>

  <div class="divider"></div>

  <p class="block format">Lecture followed by Q&amp;A<br>&amp; refreshments</p>
</main>
</body>
</html>
```